Card Design Project

We are looking for a couple card / box designs that will for a new company that is in the bereavement assistance industry.
Our customers are churches, counseling centers and funeral homes.
Once we have these card designs we will need to work with that same artist to help us out with box graphic designs that are similar to the card designs. The box is 12" long x 4" wide x 6" high
We will need more designs in the future so we are looking for an artist for future work.
Our look needs to be professional and solemn.
The front of the card should be quite close to what i am attaching but with some professional touches to it that give it a proper look. We dont want you to stray to far from what i have attached but if you feel you have some good ideas we would be more than happy to see them.
The back of the card we want people to be able to leave the family a note so will need wording such as "leave a message to the family" or "write a memory"
Keep in mind we will need this look to be able to match graphics on the box as well, we kind of need the card design and box design to go together.
Thanks
Just wanted to mention to all designers that although we would like our logo on the card it is something that we need to keep kind of in the background somehow. We cant be seen as trying to push a brand name too much so please keep that in mind. Thanks
Reason: HOLIDAY
Designers, I took the need to see what the design looked like on a box out.
Reason: just need a bit of extra time guys, thanks for all who are helping us on this!
Target Market(s)
Funeral homes, churches, counseling centers
Industry/Entity Type
Industry
Requirements
Must have
- Professional and solemn look
Card need to be 4"wide X 6" high and needs to be portrait
A pin will be attached to the top right part of the card so will need a space there for it.
I was thinking that we would have the pic of the ribbon symbol there so when the pin is off the card there would still be a ribbon pic there. The pins that we will be attaching are ribbon pins similar to what i have on my pdf's
Please keep in mind that we cant really have out logo in a dominant area on the card. We would like to have it subtly in there but not to where it is in your face type of thing.
Nice to have
- Our logo but very small, not to intrusive .
Would like 2 designs, one dark and another light.
Maybe 1 masculine or gender neutral and another feminine
Wording should be the same

```html
<!DOCTYPE html>
<html lang="en">
<head>
<meta charset="utf-8">
<title>Memorial Card – Front and Back</title>
<link rel="stylesheet" href="https://fonts.googleapis.com/css2?family=Cormorant+Infant:ital,wght@1,500;1,600&display=swap">
<style>
  :root {
    --page-bg: #ffffff;
    --card-dark: #000000;
    --card-light: #ffffff;
    --text-light: #ffffff;
    --text-dark: #111111;
    --rule-grey: #8a8a8a;
    --border-dark: #000000;
    --ribbon-grey: #5e5e5e;
    --feather-grey: #9a9a9a;
  }
  * { margin: 0; padding: 0; box-sizing: border-box; }
  html, body {
    width: 1200px; height: 857px; overflow: hidden;
    background: var(--page-bg);
  }
  .canvas { position: relative; width: 1200px; height: 857px; }

  .card-front {
    position: absolute; left: 31px; top: 34px;
    width: 537px; height: 805px;
    background: var(--card-dark);
    overflow: hidden;
    font-family: "Cormorant Infant", "Times New Roman", serif;
    font-style: italic;
    color: var(--text-light);
  }
  .ribbon-art {
    position: absolute; left: 379px; top: 31px;
    width: 115px; height: 124px;
    background: radial-gradient(ellipse at 50% 45%, var(--ribbon-grey) 0%, rgba(70,70,70,0.6) 45%, rgba(0,0,0,0) 75%);
  }
  .feather-art {
    position: absolute; left: 62px; top: 488px;
    width: 417px; height: 317px;
    background: radial-gradient(ellipse 55% 30% at 50% 32%, var(--feather-grey) 0%, rgba(110,110,110,0.55) 40%, rgba(0,0,0,0) 80%),
                radial-gradient(ellipse 45% 22% at 40% 80%, rgba(80,80,80,0.45) 0%, rgba(0,0,0,0) 80%);
  }
  .greeting {
    position: absolute; left: 0; width: 100%; top: 110px;
    padding-right: 80px;
    text-align: center;
    font-size: 36px; font-weight: 500;
  }
  .message {
    position: absolute; left: 0; width: 100%; top: 208px;
    text-align: center;
    font-size: 19px; font-weight: 600; line-height: 33.5px;
  }
  .message p + p { margin-top: 34px; }
  .thanks {
    position: absolute; left: 0; width: 100%; top: 676px;
    text-align: center;
    font-size: 19px; font-weight: 600;
  }

  .card-back {
    position: absolute; left: 644px; top: 35px;
    width: 537px; height: 806px;
    background: var(--card-light);
    border: 1.5px solid var(--border-dark);
    font-family: "Cormorant Infant", "Times New Roman", serif;
    font-style: italic;
    color: var(--text-dark);
  }
  .memory-label {
    position: absolute; left: 52px; top: 358px;
    font-size: 25px; font-weight: 600;
  }
  .memory-lines {
    position: absolute; left: 248px; top: 65px;
    width: 262px; height: 700px;
    background: repeating-linear-gradient(to bottom,
      var(--rule-grey) 0, var(--rule-grey) 1px,
      transparent 1px, transparent 31.7px);
  }
</style>
</head>
<body>
<div class="canvas">
  <section class="card-front">
    <div class="ribbon-art" role="img" aria-label="Grey awareness ribbon symbol"></div>
    <div class="feather-art" role="img" aria-label="Photograph of a grey feather reflected on a black surface"></div>
    <h1 class="greeting">Dear Friends</h1>
    <div class="message">
      <p>Your support in attending this memorial<br>and celebration of life means so much to us.</p>
      <p>Our loved one has touched you in ways<br>we may not even recognize yet.</p>
      <p>We invite you to wear this pin through<br>your grieving process, which we receive as<br>a symbol of your sympathy and support&nbsp; of our loss.</p>
    </div>
    <p class="thanks">Thank you for grieving together with us</p>
  </section>

  <section class="card-back">
    <p class="memory-label">Write a memory</p>
    <div class="memory-lines"></div>
  </section>
</div>
</body>
</html>
```